Driving School needs brochure for clients charged before the courts with Road Rage

We are a driving school who provides courses to those charged with driving with road rage. This brochure which will be a pdf trifold will be emailed to lawyers, judges and clients. Needs to be extremely professional modern and classy.

Target Market(s)

judges, lawyers

Font styles to use
Serif
Sans Serif

Requirements
Must have
• Please replicate the current Savour the Lane brochure regarding the front page and graphic.
Final design will be a single pdf document with front page of trifold at top and inner at bottom. Should look similar in deign to Steady Mindful (brown brochure) brochure. Not same color. Final panel should be very similar/identical and same as middle panel on outside of trifold (top middle panel) i.e., contact information with phone number, email and website should be similar/identical.
Should not have
• any manufacturer name/logo or image that is obviously linked

```html
<!DOCTYPE html>
<html lang="en">
<head>
<meta charset="utf-8">
<title>Road Rage – Clear Lane Driving School Trifold</title>
<link rel="stylesheet" href="https://fonts.googleapis.com/css2?family=Oswald:wght@600;700&family=Roboto+Slab:wght@400;500;700&family=Source+Sans+3:wght@400;600;700&display=swap">
<style>
:root{
  --navy-deep:#0d1a40;
  --navy:#16295c;
  --navy-mid:#203a78;
  --blue:#2f5aa6;
  --blue-soft:#5f82bd;
  --sky:#c9d7ec;
  --sky-pale:#e3ebf6;
  --ink:#17285a;
  --white:#ffffff;
  --text-soft:#d4def0;
  --stage:#e9e9e9;
  --serif:'Roboto Slab', Georgia, serif;
  --sans:'Source Sans 3', Arial, sans-serif;
  --display:'Oswald', 'Arial Narrow', sans-serif;
}
*{box-sizing:border-box;margin:0;padding:0}
html,body{width:1200px;height:2400px;overflow:hidden}
body{background:var(--stage);font-family:var(--sans);color:var(--white);position:relative}

.spread{position:absolute;left:50px;width:1100px;height:850px;display:flex;box-shadow:0 6px 24px rgba(0,0,0,.18)}
.spread--outside{top:310px}
.spread--inside{top:1240px}
.panel{position:relative;width:366.67px;height:100%;overflow:hidden}

/* shared */
.web-bar{position:absolute;left:0;right:0;bottom:22px;height:30px;background:var(--blue-soft);color:var(--white);font-family:var(--serif);font-size:14px;display:flex;align-items:center;justify-content:center;letter-spacing:.3px}
.brand{display:flex;align-items:center;justify-content:center;gap:8px;font-family:var(--serif);font-weight:700;font-size:19px;color:var(--white)}
.brand-dot{width:10px;height:10px;border-radius:50%;background:var(--white)}
.tagline{font-family:var(--serif);font-style:italic;font-size:14px;color:var(--white);text-align:center;margin-top:4px}
.services{font-family:var(--serif);font-size:14px;text-align:center;line-height:1.35;color:var(--white)}
.title{font-family:var(--display);font-weight:700;font-size:54px;line-height:1;letter-spacing:.5px;color:var(--ink)}
.subtitle{font-family:var(--serif);font-size:32px;color:var(--ink);line-height:1.1}
.heading{font-family:var(--sans);font-weight:700;font-size:14px;letter-spacing:.6px;text-transform:uppercase;color:var(--white);margin:14px 0 5px}
.body-text{font-size:12.5px;line-height:1.45;color:var(--text-soft)}
.list{list-style:none;font-size:12.5px;line-height:1.45;color:var(--text-soft)}
.list li{padding-left:12px;position:relative;margin-bottom:2px}
.list li::before{content:"";position:absolute;left:0;top:7px;width:5px;height:5px;border-radius:50%;background:var(--blue-soft)}

/* outside: background */
.panel--background{background:linear-gradient(180deg,var(--navy) 0%,var(--navy-deep) 100%);padding:34px 30px 70px}
.background-heading{font-family:var(--serif);font-style:italic;font-size:20px;color:var(--white);margin-bottom:10px}
.panel--background .body-text{margin-bottom:10px}

/* outside: contact */
.panel--contact{background:linear-gradient(180deg,var(--navy-mid) 0%,var(--navy) 60%,var(--navy-deep) 100%);padding:60px 34px 0;text-align:center}
.mission{font-family:var(--serif);font-size:28px;line-height:1.3;color:var(--white)}
.info-box{margin:34px auto 0;border:2px solid var(--text-soft);border-radius:14px;padding:26px 16px 16px;position:relative}
.info-label{position:absolute;top:-14px;left:50%;transform:translateX(-50%);background:var(--blue-soft);color:var(--white);font-weight:700;font-size:13px;letter-spacing:1px;padding:4px 14px;border-radius:4px;white-space:nowrap}
.info-phone{display:flex;align-items:center;justify-content:center;gap:10px;font-family:var(--serif);font-size:24px;color:var(--white)}
.info-line{font-family:var(--serif);font-size:15px;color:var(--white);margin-top:6px}
.panel--contact .brand-block{margin-top:34px}
.panel--contact .services{margin-top:10px;font-size:13px}

/* outside: cover */
.panel--cover{background:linear-gradient(180deg,var(--sky-pale) 0%,var(--sky) 100%)}
.cover-head{position:absolute;top:34px;left:0;right:0;text-align:center;z-index:2}
.cover-lead{font-family:var(--serif);font-size:17px;line-height:1.3;color:var(--ink);margin-top:10px}
.cover-photo{position:absolute;top:200px;left:0;right:0;height:400px;background:linear-gradient(160deg,#9fb2c8 0%,#6f7f92 45%,#3c4a5e 100%)}
.cover-band{position:absolute;left:0;bottom:0;width:100%;height:360px}
.cover-brand{position:absolute;left:0;right:0;bottom:92px;text-align:center;z-index:2}
.cover-brand .services{margin-top:18px}

/* inside: left */
.panel--overview{background:linear-gradient(180deg,var(--navy) 0%,var(--navy-deep) 100%);padding:32px 28px}
.panel--overview .title{color:var(--white);font-size:40px}
.panel--overview .subtitle{color:var(--sky);font-size:22px;margin-bottom:12px}
.sub-heading{font-weight:700;font-size:12.5px;color:var(--white);margin-top:8px;margin-bottom:2px;text-transform:uppercase}

/* inside: middle */
.panel--strategies{background:linear-gradient(180deg,var(--navy-mid) 0%,var(--navy) 100%);padding:30px 28px}
.panel--strategies .heading:first-child{margin-top:0}
.tailored-band{position:absolute;left:0;bottom:0;width:100%;height:260px}
.tailored-text{position:absolute;left:0;right:0;bottom:40px;text-align:center;font-family:var(--serif);font-size:22px;line-height:1.3;color:var(--white);z-index:2}

/* inside: right */
.panel--remote{background:linear-gradient(180deg,var(--sky-pale) 0%,var(--sky) 55%,var(--blue-soft) 100%)}
.remote-head{position:absolute;top:48px;left:40px;right:30px;display:flex;align-items:center;gap:14px}
.remote-title{font-family:var(--display);font-weight:700;font-size:34px;line-height:1;color:var(--ink)}
.remote-art{position:absolute;top:140px;left:36px;right:36px;height:180px;border-radius:10px;background:linear-gradient(135deg,#f4f7fb 0%,#b9cbe6 100%)}
.price{position:absolute;top:340px;left:50%;transform:translateX(-50%);display:flex;align-items:center;background:var(--navy);border-radius:6px;overflow:hidden;white-space:nowrap}
.price-label{background:var(--blue);font-size:13px;font-weight:600;padding:8px 10px}
.price-value{font-family:var(--serif);font-size:19px;padding:6px 14px}
.remote-band{position:absolute;left:0;bottom:0;width:100%;height:420px}
.remote-brand{position:absolute;left:0;right:0;bottom:70px;text-align:center;z-index:2}
.remote-brand .services{margin-top:36px;font-size:16px}
</style>
</head>
<body>

<!-- OUTSIDE SPREAD -->
<section class="spread spread--outside">
  <article class="panel panel--background">
    <h2 class="background-heading">Our background:</h2>
    <p class="body-text">Since its inception in 1998, Clear Lane Driving School has helped drivers of every age regain confidence on the road. Our instructors offer safety-focused training, with qualified staff guiding each student through lessons suited to their needs and goals.</p>
    <p class="body-text">We have supported new drivers, seniors and those returning to the road after a medical event or a serious incident. Our team works closely with clinics, lawyers and families to make each plan clear, fair and practical for the learner.</p>
    <p class="body-text">Clear Lane has also developed courses for drivers facing charges, blending classroom learning with time behind the wheel. Programs are reviewed often so content stays current with provincial law and research.</p>
    <p class="body-text">Today our school offers instruction in person and online, with flexible hours and private sessions for all learners.</p>
    <div class="web-bar">www.clearlanedriving.ca</div>
  </article>

  <article class="panel panel--contact">
    <p class="mission">Maintaining driving independence, while leading safe and productive lives!</p>
    <div class="info-box">
      <span class="info-label">FOR MORE INFORMATION</span>
      <p class="info-phone">
        <svg width="24" height="24" viewBox="0 0 24 24" aria-hidden="true"><path d="M6.6 10.8a15.1 15.1 0 0 0 6.6 6.6l2.2-2.2c.3-.3.7-.4 1-.2 1.1.4 2.3.6 3.6.6.6 0 1 .4 1 1V20c0 .6-.4 1-1 1A17 17 0 0 1 3 4c0-.6.4-1 1-1h3.5c.6 0 1 .4 1 1 0 1.3.2 2.5.6 3.6.1.3 0 .7-.2 1l-2.3 2.2z" fill="#fff"/></svg>
        555-014-2270
      </p>
      <p class="info-line">www.clearlanedriving.ca</p>
      <p class="info-line">hello@clearlanedriving.ca</p>
    </div>
    <div class="brand-block">
      <p class="brand"><span class="brand-dot"></span>Clear Lane Driving School</p>
      <p class="tagline">Making drivers safe... for life!</p>
      <p class="services">For all your G License needs!<br>Beginner, Rehabilitation &amp; Remedial</p>
    </div>
    <div class="web-bar">www.clearlanedriving.ca</div>
  </article>

  <article class="panel panel--cover">
    <header class="cover-head">
      <h1 class="title">ROAD RAGE</h1>
      <p class="subtitle">Savour the Lane</p>
      <p class="cover-lead">A 1-day educational course for those<br>charged with Road Rage.</p>
    </header>
    <div class="cover-photo" role="img" aria-label="Photo of a frustrated driver shouting behind the steering wheel"></div>
    <svg class="cover-band" viewBox="0 0 367 360" preserveAspectRatio="none" aria-hidden="true">
      <path d="M0 150 Q180 40 367 20 L367 360 L0 360 Z" fill="#5f82bd"/>
      <path d="M0 170 Q180 64 367 44 L367 360 L0 360 Z" fill="#16295c"/>
    </svg>
    <div class="cover-brand">
      <p class="brand"><span class="brand-dot"></span>Clear Lane Driving School</p>
      <p class="tagline">Making drivers safe... for life!</p>
      <p class="services">For all your G License needs!<br>Beginner, Rehabilitation &amp; Remedial</p>
    </div>
    <div class="web-bar">www.clearlanedriving.ca</div>
  </article>
</section>

<!-- INSIDE SPREAD -->
<section class="spread spread--inside">
  <article class="panel panel--overview">
    <h2 class="title">ROAD RAGE</h2>
    <p class="subtitle">Savour the Lane</p>
    <p class="body-text">A 1-day, 7-hour, intensive remedial awareness course for those charged with road rage.</p>
    <p class="body-text" style="margin-top:8px">Our goal is to equip our customers with knowledge and tools to help them avoid escalating and dangerous behaviour behind the wheel in the future.</p>
    <h3 class="heading">Topics covered:</h3>
    <p class="sub-heading">Law:</p>
    <ul class="list">
      <li>Highway Traffic Act penalties &amp; rights</li>
      <li>Federal and Provincial law</li>
      <li>Implications of criminal record (financial, work, relationships, etc.)</li>
    </ul>
    <p class="sub-heading">Road rage:</p>
    <ul class="list">
      <li>Triggers</li>
      <li>Personality types (Type A), drivers &amp; stress scales</li>
      <li>Aggressive driving overlap between aggression and driving</li>
      <li>Post traumatic stress and driving, a link to fears</li>
    </ul>
    <p class="sub-heading">Physiology and the negative impacts of stress on the body</p>
    <ul class="list">
      <li>Fight or flight response: how it works</li>
      <li>Hormones (adrenaline, cortisol, etc.)</li>
      <li>Chronic levels of stress, immune system</li>
      <li>Substances with a brief overview of drinking and driving</li>
    </ul>
  </article>

  <article class="panel panel--strategies">
    <h3 class="heading">Strategies to manage:</h3>
    <ul class="list">
      <li>Models of anger: stages to help prevent outbursts</li>
      <li>Breathing tools to calm the body and mind</li>
      <li>Stress diaries and the triggers that set you off</li>
      <li>Mindful driving, planning routes and timing</li>
      <li>Cognitive shifts: 'let it go' thinking in traffic</li>
    </ul>
    <h3 class="heading">Personal context:</h3>
    <ul class="list">
      <li>Genetic &amp; family patterns of anger</li>
      <li>Personal triggers leading up to the event, what it meant, what you can change</li>
    </ul>
    <h3 class="heading">Intensive driving skills:</h3>
    <ul class="list">
      <li>The golden rule: following distance</li>
      <li>Defensive driving with space around the car</li>
      <li>Using your eyes and strategic scanning</li>
      <li>Driving in heavy traffic calmly and safely</li>
    </ul>
    <svg class="tailored-band" viewBox="0 0 367 260" preserveAspectRatio="none" aria-hidden="true">
      <path d="M0 80 Q190 10 367 60 L367 260 L0 260 Z" fill="#2f5aa6"/>
      <path d="M0 100 Q190 34 367 82 L367 260 L0 260 Z" fill="#203a78"/>
    </svg>
    <p class="tailored-text">Courses are<br>individually<br>tailored<br>ONE-ON-ONE.</p>
  </article>

  <article class="panel panel--remote">
    <div class="remote-head">
      <svg width="50" height="44" viewBox="0 0 50 44" aria-hidden="true"><rect x="2" y="2" width="46" height="30" rx="5" fill="none" stroke="#17285a" stroke-width="3"/><path d="M14 32 L10 42 L24 32" fill="#17285a"/><circle cx="15" cy="17" r="2.5" fill="#17285a"/><circle cx="25" cy="17" r="2.5" fill="#17285a"/><circle cx="35" cy="17" r="2.5" fill="#17285a"/></svg>
      <p class="remote-title">OFFERED<br>REMOTELY!</p>
    </div>
    <div class="remote-art" role="img" aria-label="Illustration of an online class on a laptop screen with an instructor"></div>
    <div class="price"><span class="price-label">Course Cost</span><span class="price-value">$775.00 + HST</span></div>
    <svg class="remote-band" viewBox="0 0 367 420" preserveAspectRatio="none" aria-hidden="true">
      <path d="M0 190 Q200 70 367 50 L367 420 L0 420 Z" fill="#5f82bd"/>
      <path d="M0 212 Q200 94 367 74 L367 420 L0 420 Z" fill="#16295c"/>
    </svg>
    <div class="remote-brand">
      <p class="brand"><span class="brand-dot"></span>Clear Lane Driving School</p>
      <p class="tagline">Making drivers safe... for life!</p>
      <p class="services">For all your G License needs!<br>Beginner, Rehabilitation &amp; Remedial</p>
    </div>
  </article>
</section>

</body>
</html>
```